Stationery Design Project

We are looking for a full revision of our existing stationary to include within this project:

- Letterhead
- Business card
- Compliment slip

The items should be a reflection of our new website which can be found at http://www.larkfieldchecks.co.uk/

Our logo files are included within the file brief

There are some further projects which we may approach the winning designer for as we need a revision to the front cover of our reports, a new price list and two brochures for specific target markets.

Industry/Entity Type

Business

```html
<!DOCTYPE html>
<html lang="en">
<head>
<meta charset="utf-8">
<title>Larkfield Checks — Stationery</title>
<link href="https://fonts.googleapis.com/css2?family=Open+Sans:wght@400;600&family=PT+Sans&display=swap" rel="stylesheet">
<style>
:root{
  --stage:#000;
  --paper:#fff;
  --brand:#27237f;
  --accent:#2f6fb7;
  --ink:#333;
  --muted:#8a8a8a;
  --fade-top:#ffffff;
  --fade-bottom:#dcdcdc;
  --card-light:#1d9be0;
  --card-dark:#1a4f9c;
}
*{box-sizing:border-box;margin:0;padding:0}
html,body{width:1200px;height:900px;overflow:hidden;background:var(--stage)}
body{position:relative;font-family:"Open Sans",sans-serif;color:var(--ink)}
.sheet{position:absolute;background:var(--paper);overflow:hidden}

.brand{display:flex;align-items:center;gap:6px;color:var(--brand);font-family:"Open Sans",sans-serif;font-weight:600;text-transform:uppercase;letter-spacing:.5px;white-space:nowrap}
.brand-dot{width:7px;height:7px;border-radius:50%;background:var(--brand)}
.brand--light{color:#fff}
.brand--light .brand-dot{background:#fff}

.footer-band{position:absolute;left:0;right:0;bottom:0;background:linear-gradient(180deg,var(--fade-top),var(--fade-bottom))}

/* Letterhead */
.letterhead{left:96px;top:60px;width:612px;height:792px}
.letterhead .brand{position:absolute;left:34px;top:60px;font-size:19px}
.sender{position:absolute;left:458px;top:44px;font-size:9px;line-height:12px;color:var(--muted)}
.sender b{font-weight:400;color:var(--accent)}
.sender .web{color:var(--accent)}
.letter-body{position:absolute;left:92px;top:245px;width:448px;font-family:"PT Sans",sans-serif;font-size:9.3px;line-height:10.6px;color:#222;text-align:justify}
.letter-body p{margin-bottom:10.6px}
.signature{position:absolute;left:104px;top:562px;width:100px;height:74px;background:linear-gradient(135deg,#f4f4f4,#e6e6e6)}
.letterhead .footer-band{height:72px}

/* Business card */
.card{width:252px;height:144px}
.card-back{left:790px;top:96px;background:radial-gradient(ellipse at 80% 70%,var(--card-light),var(--card-dark) 80%)}
.card-back .brand{position:absolute;right:14px;bottom:12px;font-size:11px}
.card-back .card-wave{position:absolute;left:0;right:0;bottom:0;height:26px;background:linear-gradient(180deg,rgba(255,255,255,0),rgba(255,255,255,.18))}
.card-front{left:790px;top:246px}
.card-front .brand{position:absolute;left:10px;top:16px;font-size:11px}
.card-holder{position:absolute;left:26px;top:83px}
.card-holder .name{font-size:9px;color:var(--accent);font-weight:600}
.card-holder .role{font-size:5.5px;color:var(--muted)}
.card-divider{position:absolute;left:123px;top:60px;width:1px;height:68px;background:#bbb}
.card-contact{position:absolute;left:140px;top:63px;font-size:5.5px;line-height:8px;color:var(--muted);list-style:none}
.card-contact li{display:flex;align-items:center;gap:3px}
.card-contact .gap{height:8px}
.card-contact svg{width:5px;height:5px;fill:var(--accent)}
.card-front .footer-band{height:26px}

/* Compliment slip */
.comp-slip{left:492px;top:474px;width:633px;height:276px;box-shadow:0 0 6px rgba(255,255,255,.5)}
.comp-slip .brand{position:absolute;left:22px;top:38px;font-size:17px}
.comp-slip .sender{left:26px;top:94px;font-size:9px}
.comp-title{position:absolute;right:32px;top:219px;font-size:21px;font-weight:400;color:var(--accent)}
.comp-slip .footer-band{height:56px;z-index:0}
.comp-title{z-index:1}
</style>
</head>
<body>

<section class="sheet letterhead" aria-label="Letterhead">
  <div class="brand"><span>Larkfield Checks</span><span class="brand-dot"></span></div>
  <address class="sender" style="font-style:normal">
    418 Orchard Lane<br>
    Unit 12 Maidstone, ME16 4AB<br>
    <b>Phone.</b> (01622) 555-0148<br>
    <b>Fax.</b> (01622) 555-0148<br>
    <span class="web">www.larkfieldchecks.co.uk</span>
  </address>
  <div class="letter-body">
    <p>In dui turpis, varius vitae, tincidunt id, consequat ut, leo. Donec tincidunt tristique odio. Nulla erat felis, euismod nec, fringilla non, aliquet et, magna. Nulla at magna quis nisi pretium vehicula. Pellentesque habitant morbi tristique senectus et netus et malesuada fames ac turpis egestas. Class aptent taciti sociosqu ad litora torquent per conubia nostra, per inceptos himenaeos. In vel quam. Phasellus varius convallis purus. In non turpis. Nam sed risus. Etiam non neque at nisl gravida porttitor. Donec leo dolor, feugiat ut, pharetra et, porttitor a, metus. Suspendisse laoreet magna vel elit. Ut est augue, fermentum ac, molestie at, vestibulum et, urna.</p>
    <p>Nunc purus. Cras auctor. In ornare neque id ipsum. Nulla tincidunt, diam sit amet viverra euismod, sapien augue fringilla neque, at pellentesque felis tortor vel enim. Etiam dignissim. Sed a tortor vel nisl euismod ultricies. Donec molestie congue lectus. Integer sed turpis a tortor imperdiet consequat. Maecenas molestie placerat urna. Sed pede enim, sollicitudin nec, pretium nec, sollicitudin a, felis. In hac habitasse platea dictumst. Nam facilisis, tellus non scelerisque placerat, turpis turpis semper ante, euismod imperdiet augue nisi et neque. Vivamus tincidunt.</p>
    <p>Nulla lobortis ultricies nulla. Pellentesque purus mi, consequat quis, hendrerit sed, imperdiet non, eros. Nullam urna est, vehicula nec, cursus nec, dignissim et, tortor. Proin vehicula tellus sit amet laoreet ullamcorper, urna nisi fringilla ante, at rhoncus lorem tortor at nunc hendrerit luctus lorem. Aenean tempor, metus vel posuere gravida, est massa blandit sem magna a turpis. Vivamus in neque. Lorem ipsum dolor sit amet, consectetuer adipiscing elit. Duis tristique tortor id nisl feugiat posuere. Maecenas pretium, massa et hendrerit. Praesent porta tempus ligula. Morbi in leo. Curabitur sed quam vitae bus in, porttitor et, odio. Praesent sed justo sed arcu commodo feugiat ut nec ligula. Cras libero. Donec mollis consectetuer metus. Praesent odio.</p>
  </div>
  <div class="signature" role="img" aria-label="Handwritten signature"></div>
  <div class="footer-band" role="img" aria-label="Faint rooftop decoration along the bottom edge"></div>
</section>

<section class="sheet card card-back" aria-label="Business card, back">
  <div class="card-wave" role="img" aria-label="Faint rooftop decoration"></div>
  <div class="brand brand--light"><span>Larkfield Checks</span><span class="brand-dot"></span></div>
</section>

<section class="sheet card card-front" aria-label="Business card, front">
  <div class="brand"><span>Larkfield Checks</span><span class="brand-dot"></span></div>
  <div class="card-holder">
    <div class="name">Ellis Marren</div>
    <div class="role">Managing Director</div>
  </div>
  <div class="card-divider"></div>
  <ul class="card-contact">
    <li>27 Wharf Road</li>
    <li>Maidstone, ME15 6RP</li>
    <li class="gap"></li>
    <li><svg viewBox="0 0 10 10"><path d="M2 1l2 0 1 3-1.5 1a6 6 0 0 0 2.5 2.5L7 6l3 1v2C4 10 0 6 1 1z"/></svg>(01622) 555-0190</li>
    <li><svg viewBox="0 0 10 10"><rect x="1" y="2" width="8" height="6"/></svg>(01622) 555-0148</li>
    <li><svg viewBox="0 0 10 10"><path d="M1 2h8v6H1z M1 2l4 3 4-3" fill="none" stroke="#2f6fb7"/></svg>ellis@larkfieldchecks.co.uk</li>
    <li><svg viewBox="0 0 10 10"><circle cx="5" cy="5" r="4"/></svg>www.larkfieldchecks.co.uk</li>
  </ul>
  <div class="footer-band" role="img" aria-label="Faint rooftop decoration"></div>
</section>

<section class="sheet comp-slip" aria-label="Compliment slip">
  <div class="brand"><span>Larkfield Checks</span><span class="brand-dot"></span></div>
  <address class="sender" style="font-style:normal">
    418 Orchard Lane<br>
    Unit 12 Maidstone, ME16 4AB
  </address>
  <div class="footer-band" role="img" aria-label="Faint rooftop decoration along the bottom edge"></div>
  <h2 class="comp-title">With Compliments</h2>
</section>

</body>
</html>
```